Vesk Architecture

We are a architectural design and build company working between scales 1/1000 to 1/1 we want people to understand our difference from our design experience and quality.we build hotels restourants and office spaces.Our company name is Vesk architecture to mind sustainability.

We want to write our adress phone and work spesifications on the card and we want our logo as backround.

Ps:you could find the logo adress and phone box numbers from the web:www.veskmimarlik-ornek.com

Target Market(s)

Who looks for experts.

Industry/Entity Type

Architecture

Requirements
Must have
• Design is over everything.
Should not have
• we don want it to be colorfull

```html
<!DOCTYPE html>
<html lang="tr">
<head>
<meta charset="utf-8">
<title>Vesk Mimarlik – Business Card</title>
<link rel="stylesheet" href="https://fonts.googleapis.com/css2?family=Arimo:wght@400;700&display=swap">
<style>
  :root {
    --stage: #000000;
    --card-blue: #bcd6e8;
    --card-white: #ffffff;
    --ink: #111111;
    --mark-blue: #bcd6e8;
  }
  html, body {
    margin: 0;
    padding: 0;
    width: 1200px;
    height: 899px;
    overflow: hidden;
    background: var(--stage);
  }
  .stage {
    position: relative;
    width: 1200px;
    height: 899px;
    font-family: "Arimo", Helvetica, Arial, sans-serif;
  }
  .card {
    position: absolute;
    left: 344px;
    width: 508px;
    height: 327px;
    overflow: hidden;
  }
  .card--front { top: 107px; background: var(--card-blue); }
  .card--back  { top: 471px; background: var(--card-white); }

  .holder-name {
    position: absolute;
    top: 26px;
    right: 24px;
    margin: 0;
    font-weight: 700;
    font-size: 19px;
    letter-spacing: 0.6px;
    color: var(--ink);
  }
  .wordmark {
    position: absolute;
    margin: 0;
    font-weight: 400;
    line-height: 1;
  }
  .wordmark span { display: block; }
  .card--front .wordmark {
    left: 18px;
    top: 34px;
    color: var(--card-white);
  }
  .card--front .wordmark__name { font-size: 190px; letter-spacing: -4px; }
  .card--front .wordmark__sub  { font-size: 48px; letter-spacing: 4px; margin-top: 4px; }

  .card--back .wordmark {
    left: 0;
    right: 0;
    top: 14px;
    text-align: center;
    color: var(--mark-blue);
  }
  .card--back .wordmark__name { font-size: 96px; letter-spacing: -2px; }
  .card--back .wordmark__sub  { font-size: 25px; letter-spacing: 2.5px; margin-top: 2px; }

  .contact {
    position: absolute;
    left: 0;
    right: 0;
    top: 188px;
    margin: 0;
    text-align: center;
    font-style: normal;
    font-size: 19px;
    letter-spacing: 1.2px;
    color: var(--ink);
    line-height: 25px;
  }
  .contact__lines { display: block; }
  .contact__phones { display: block; margin-top: 9px; }
  .contact__phones span + span { margin-left: 24px; }
  .contact__mail { display: block; margin-top: 8px; }
</style>
</head>
<body>
<main class="stage">
  <section class="card card--front" aria-label="Card front">
    <p class="holder-name">Deniz Kaya</p>
    <h1 class="wordmark">
      <span class="wordmark__name">vesk</span>
      <span class="wordmark__sub">MIMARLIK</span>
    </h1>
  </section>

  <section class="card card--back" aria-label="Card back">
    <h2 class="wordmark">
      <span class="wordmark__name">vesk</span>
      <span class="wordmark__sub">MIMARLIK</span>
    </h2>
    <address class="contact">
      <span class="contact__lines">Yeldegirmeni Mah. Cinar Cad. Ayva Sok<br>No:7 Kadikoy/Istanbul</span>
      <span class="contact__phones"><span>T.0216 555 01 47</span><span>F.0216 555 01 48</span></span>
      <span class="contact__mail">E-mail: veskmimarlik@ornek-mail.com</span>
    </address>
  </section>
</main>
</body>
</html>
```